Business Card For Talent Company
BLITZ Talent
Project: Business Card For Talent Company
Business Card For Talent Company - Entertainment
Creative Brief
Cutting-Edge
Lorna Pidge
Talent Development
2734 W. Ferncastle Rd. Dovermill Park IL 60419
blitztalent@quorvex.com
www.blitztalent-quorvex.com
Are you ready to break through?
Kelvorn Kelvorn
We are really desperate to see some fun contemporary and modern designs...we are a talent company...would really like to see something innovative and not so corporate looking.....thank you!
Aquamarine/Teal Shade of Blue Please!....We really want something fun and edgy....these are too corporate looking...
We are a talent agency....really looking for something cool and cutting edge for our company...the shade of blue is coming through wrong on the logo...we are looking for a more like a teal blue color....thank you!
Our Tag Line "are you ready to break through" needs to be on all of the materials....thank you!
we are looking for more of teal shade of blue..I uploaded our other logo....
This contest is for full stationary...
It is both business card and stationary that we are needing....thank you!

```html
<!DOCTYPE html>
<html lang="en">
<head>
<meta charset="utf-8">
<title>BLITZ Talent — Business Card</title>
<link rel="stylesheet" href="https://fonts.googleapis.com/css2?family=Michroma&display=swap">
<style>
  :root {
    --page-bg: #e9e9eb;
    --card-black: #0c0c0e;
    --band-dark: #0d5f69;
    --band-mid: #168f98;
    --band-light: #35b8b6;
    --icon-ink: #137c85;
    --ink-white: #f4f8f8;
    --ink-soft: #dff3f2;
    --ink-teal: #5fd0cb;
  }
  * { box-sizing: border-box; margin: 0; padding: 0; }
  html, body {
    width: 1200px; height: 902px; overflow: hidden;
    background: var(--page-bg);
  }
  body { position: relative; font-family: "Michroma", sans-serif; }

  .business-card {
    position: absolute; left: 100px; top: 165px;
    width: 1000px; height: 572px;
    background: var(--card-black);
    border-radius: 6px;
    overflow: hidden;
  }
  .brand {
    position: absolute; left: 80px; top: 128px;
    display: flex; align-items: center; gap: 18px;
  }
  .brand-mark {
    width: 22px; height: 22px; background: var(--ink-white);
  }
  .brand-name {
    color: var(--ink-white);
    font-size: 46px; letter-spacing: 2px;
    line-height: 1; white-space: nowrap;
  }
  .contact-band {
    position: absolute; left: 0; top: 236px;
    width: 100%; height: 250px;
    background: linear-gradient(90deg, var(--band-dark) 0%, var(--band-mid) 45%, var(--band-light) 70%, var(--band-mid) 100%);
  }
  .band-tab {
    position: absolute; left: 0; top: 120px;
    width: 12px; height: 62px;
    background: var(--ink-white);
    border-radius: 0 5px 5px 0;
  }
  .holder {
    position: absolute; left: 48px; top: 122px;
    color: var(--ink-white);
    white-space: nowrap;
  }
  .holder-name { font-size: 19px; letter-spacing: 1px; }
  .holder-role { font-size: 14px; margin-top: 14px; color: var(--ink-soft); letter-spacing: 0.5px; }

  .contact-list {
    position: absolute; left: 560px; top: 18px;
    list-style: none;
    color: var(--ink-white);
    font-size: 14px; letter-spacing: 1px; text-transform: uppercase;
    white-space: nowrap;
  }
  .contact-list li { display: flex; align-items: flex-start; gap: 10px; line-height: 27px; }
  .contact-list .indent { padding-left: 30px; }
  .contact-icon { width: 20px; height: 20px; flex: none; margin-top: 3px; }

  .tagline {
    position: absolute; left: 80px; top: 516px;
    color: var(--ink-teal);
    font-size: 15px; letter-spacing: 2px;
    white-space: nowrap;
  }
</style>
</head>
<body>
  <article class="business-card">
    <div class="brand">
      <span class="brand-mark"></span>
      <span class="brand-name">BLITZ Talent</span>
    </div>

    <section class="contact-band">
      <span class="band-tab"></span>

      <div class="holder">
        <p class="holder-name">Lorna Pidge</p>
        <p class="holder-role">Talent Development</p>
      </div>

      <ul class="contact-list">
        <li>
          <svg class="contact-icon" viewBox="0 0 20 20"><circle cx="10" cy="10" r="10" fill="#f4f8f8"/><path d="M10 4a4 4 0 0 0-4 4c0 3 4 8 4 8s4-5 4-8a4 4 0 0 0-4-4z" fill="#137c85"/><circle cx="10" cy="8" r="1.5" fill="#f4f8f8"/></svg>
          <span>2734 W. Ferncastle Rd.</span>
        </li>
        <li class="indent"><span>Dovermill Park IL 60419</span></li>
        <li>
          <svg class="contact-icon" viewBox="0 0 20 20"><circle cx="10" cy="10" r="10" fill="#f4f8f8"/><path d="M6.5 5h2l1 3-1.3 1a7 7 0 0 0 3 3l1-1.3 3 1v2c0 .6-.5 1-1 1A9 9 0 0 1 5.5 6c0-.5.4-1 1-1z" fill="#137c85"/></svg>
          <span>312.555.0147</span>
        </li>
        <li>
          <svg class="contact-icon" viewBox="0 0 20 20"><circle cx="10" cy="10" r="10" fill="#f4f8f8"/><rect x="7" y="4" width="6" height="12" rx="1.2" fill="#137c85"/><rect x="8" y="5.5" width="4" height="7" fill="#f4f8f8"/></svg>
          <span>847.555.0193</span>
        </li>
        <li>
          <svg class="contact-icon" viewBox="0 0 20 20"><circle cx="10" cy="10" r="10" fill="#f4f8f8"/><rect x="5" y="6.5" width="10" height="7" fill="#137c85"/><path d="M5 6.5l5 4 5-4" stroke="#f4f8f8" stroke-width="1" fill="none"/></svg>
          <span>blitztalent@quorvex.com</span>
        </li>
        <li>
          <svg class="contact-icon" viewBox="0 0 20 20"><circle cx="10" cy="10" r="10" fill="#f4f8f8"/><circle cx="10" cy="10" r="5.5" fill="none" stroke="#137c85" stroke-width="1.3"/><path d="M4.5 10h11M10 4.5c-2.5 3-2.5 8 0 11M10 4.5c2.5 3 2.5 8 0 11" stroke="#137c85" stroke-width="1.1" fill="none"/></svg>
          <span>www.blitztalent-quorvex.com</span>
        </li>
      </ul>
    </section>

    <p class="tagline">Are you ready to break through?</p>
  </article>
</body>
</html>
```